Dolan's Auto Business Card
Dolan's Auto Letter Head
Professional
Kevan Dookhoo, MBA, L.L.B.
Managing Director
Corvale Shopping Plaza
14 Tennant Ave
East Merivale, Carova
kevanmail@qorvamail.com
www.dolansauto.com
additional email: kevan@dolansauto.com
LOGO
Drive Open Lead Aim Nurture (D.O.L.A.N)

```html
<!DOCTYPE html>
<html lang="en">
<head>
<meta charset="utf-8">
<title>Dolan's Auto Business Card</title>
<link href="https://fonts.googleapis.com/css2?family=Arimo:wght@400;700&display=swap" rel="stylesheet">
<style>
  :root{
    --page:#e9ebee;
    --card-white:#ffffff;
    --brand-blue:#1c5fb0;
    --deep-blue:#0b3f8c;
    --light-blue:#3f98dc;
    --brand-green:#3f9a2a;
    --light-green:#8cc63f;
    --deep-green:#2a6e1c;
    --brand-red:#e3222b;
    --ink:#333333;
    --white:#ffffff;
  }
  html,body{margin:0;padding:0;overflow:hidden;}
  body{
    width:1200px;height:702px;background:var(--page);
    font-family:"Arimo",Arial,sans-serif;position:relative;
  }
  .card{
    position:absolute;width:552px;border-radius:16px;overflow:hidden;
    box-shadow:0 0 0 1px #c9ccd1;
  }
  .card--front{left:29px;top:29px;height:307px;background:var(--card-white);}
  .card--blue{left:619px;top:29px;height:307px;
    background:radial-gradient(ellipse at 35% 25%,var(--light-blue) 0%,var(--brand-blue) 55%,var(--deep-blue) 100%);}
  .card--white-back{left:29px;top:360px;height:312px;background:var(--card-white);}
  .card--green{left:619px;top:360px;height:312px;
    background:radial-gradient(ellipse at 50% 40%,var(--light-green) 0%,var(--brand-green) 60%,var(--deep-green) 100%);}

  .wave{position:absolute;left:0;top:0;width:552px;height:307px;}

  .brand{display:flex;align-items:center;gap:8px;}
  .brand__dot{border-radius:50%;background:var(--brand-green);flex:none;}
  .brand__name{color:var(--brand-red);font-weight:700;white-space:nowrap;}

  .brand--small{position:absolute;left:14px;top:40px;}
  .brand--small .brand__dot{width:34px;height:34px;}
  .brand--small .brand__name{font-size:22px;}

  .holder{position:absolute;left:208px;top:86px;color:var(--brand-blue);}
  .holder__name{font-size:21px;margin:0;font-weight:400;white-space:nowrap;line-height:24px;}
  .holder__role{font-size:12.5px;color:var(--ink);margin:4px 0 0 88px;white-space:nowrap;}

  .contact{position:absolute;left:16px;top:190px;color:var(--white);font-size:12.5px;line-height:16px;}
  .contact p{margin:0;white-space:nowrap;}

  .brand--large{position:absolute;left:0;right:0;top:105px;justify-content:center;}
  .brand--large .brand__dot{width:92px;height:92px;}
  .brand--large .brand__name{font-size:50px;}
  .card--blue .brand__dot,.card--green .brand__dot{box-shadow:0 0 0 3px rgba(255,255,255,.85);}

  .tagline{position:absolute;left:0;right:0;bottom:30px;margin:0;text-align:center;font-size:13px;}
  .card--blue .tagline,.card--green .tagline{color:var(--white);}
  .card--white-back .tagline{color:var(--ink);}
</style>
</head>
<body>

<section class="card card--front">
  <svg class="wave" viewBox="0 0 552 307" aria-hidden="true">
    <defs>
      <linearGradient id="bandBlue" x1="0" y1="0" x2="1" y2="1">
        <stop offset="0" stop-color="#2f7fd0"/>
        <stop offset="1" stop-color="#0b3f8c"/>
      </linearGradient>
    </defs>
    <path d="M0 165 C140 157 250 182 340 167 C430 153 500 128 552 110 L552 307 L0 307 Z" fill="url(#bandBlue)"/>
    <path d="M0 157 C140 149 250 173 340 157 C430 143 500 118 552 98" fill="none" stroke="#8cc63f" stroke-width="4"/>
  </svg>
  <div class="brand brand--small">
    <span class="brand__dot"></span>
    <span class="brand__name">Dolan's Auto</span>
  </div>
  <div class="holder">
    <h1 class="holder__name">Kevan Dookhoo, MBA, L.L.B.</h1>
    <p class="holder__role">Managing Director</p>
  </div>
  <div class="contact">
    <p>Corvale Shopping Plaza, 14 Tennant Ave</p>
    <p>East Merivale, Carova</p>
    <p>Toll free: (305) 555-0148 | PhoneL: (868) 555-0172</p>
    <p>Cell: (868) 555-0193/ (954) 555-0126</p>
    <p>Email: kevanmail@qorvamail.com | Email: kevan@dolansauto.com</p>
    <p>www.dolansauto.com</p>
  </div>
</section>

<section class="card card--blue">
  <div class="brand brand--large">
    <span class="brand__dot"></span>
    <span class="brand__name">Dolan's Auto</span>
  </div>
  <p class="tagline">Drive Open Lead Aim Nurture (D.O.L.A.N)</p>
</section>

<section class="card card--white-back">
  <div class="brand brand--large">
    <span class="brand__dot"></span>
    <span class="brand__name">Dolan's Auto</span>
  </div>
  <p class="tagline">Drive Open Lead Aim Nurture (D.O.L.A.N)</p>
</section>

<section class="card card--green">
  <div class="brand brand--large">
    <span class="brand__dot"></span>
    <span class="brand__name">Dolan's Auto</span>
  </div>
  <p class="tagline">Drive Open Lead Aim Nurture (D.O.L.A.N)</p>
</section>

</body>
</html>
```